KALVERIA Consultancy Business Card

We need a business card design for a new Image & Etiquette Consultancy Company.

The design should reflect the corporate colour found in the logo attached.

Info to include:

Name: Melba Tran
Title: Image Consultant
Company: KAL VERIA CONSULTANCY
Address: 27 Kelso Street, #14-09 Harbourline Tower, Singapore 058217
Contact: 9317 6284
Email: melba@kalveria.com.sg
Website: www.kalveria.com.sg

```html
<!DOCTYPE html>
<html lang="en">
<head>
<meta charset="utf-8">
<title>KALVERIA Consultancy Business Card</title>
<link href="https://fonts.googleapis.com/css2?family=Carlito:wght@400;700&display=swap" rel="stylesheet">
<style>
  :root {
    --backdrop: #6a3b1f;
    --card: #ffffff;
    --brand-purple: #2e1848;
    --brand-gold: #c59d35;
    --ink: #1a1a1a;
    --ghost: #e7e7e9;
  }
  * { margin: 0; padding: 0; box-sizing: border-box; }
  html, body {
    width: 1200px;
    height: 902px;
    overflow: hidden;
    background: var(--backdrop);
    font-family: "Carlito", "Calibri", sans-serif;
  }
  .stage { position: relative; width: 1200px; height: 902px; }

  .card {
    position: absolute;
    background: var(--card);
    overflow: hidden;
  }
  .card--front { left: 40px; top: 34px; width: 699px; height: 398px; }
  .card--back  { left: 462px; top: 464px; width: 700px; height: 400px; }

  .brand-name {
    position: absolute;
    color: var(--brand-purple);
    font-weight: 400;
    line-height: 1;
    white-space: nowrap;
  }
  .card--front .brand-name {
    left: 36px;
    top: 40px;
    font-size: 52px;
    letter-spacing: 10px;
  }
  .card--back .brand-name {
    left: 0; right: 0;
    top: 146px;
    text-align: center;
    font-size: 60px;
    letter-spacing: 16px;
    padding-left: 16px;
  }

  .person {
    position: absolute;
    left: 36px;
    top: 150px;
    color: var(--ink);
  }
  .person__name { font-size: 22px; font-weight: 700; }
  .person__title { font-size: 17px; margin-left: 4px; }

  .contacts {
    position: absolute;
    left: 36px;
    top: 208px;
    list-style: none;
    font-size: 17px;
    color: var(--ink);
  }
  .contacts li { display: flex; align-items: center; height: 23px; }
  .contacts svg { width: 14px; height: 14px; margin-right: 10px; flex: none; }

  .address {
    position: absolute;
    left: 36px;
    top: 300px;
    font-size: 17px;
    line-height: 23.5px;
    font-style: normal;
    color: var(--ink);
  }

  .ghost-name {
    position: absolute;
    left: 392px;
    top: 338px;
    font-size: 56px;
    letter-spacing: 3px;
    color: var(--ghost);
    white-space: nowrap;
    line-height: 1;
  }

  .website {
    position: absolute;
    left: 0; right: 0;
    top: 337px;
    text-align: center;
    font-size: 21px;
    color: var(--ink);
  }
</style>
</head>
<body>
<main class="stage">

  <section class="card card--front" aria-label="Business card front">
    <span class="brand-name">KALVERIA</span>

    <p class="person">
      <span class="person__name">Melba Tran</span>
      <span class="person__title">Image Consultant</span>
    </p>

    <ul class="contacts">
      <li>
        <svg viewBox="0 0 14 14" aria-hidden="true"><path d="M3 1.5h2.2l1 3-1.4 1.2a7 7 0 0 0 3.5 3.5l1.2-1.4 3 1V11a1.5 1.5 0 0 1-1.5 1.5A10 10 0 0 1 1.5 3 1.5 1.5 0 0 1 3 1.5z" fill="var(--brand-gold)"/></svg>
        9317 6284
      </li>
      <li>
        <svg viewBox="0 0 14 14" aria-hidden="true"><rect x="1" y="3" width="12" height="8.5" rx="1" fill="var(--brand-gold)"/><path d="M1.5 3.6 7 8l5.5-4.4" stroke="#fff" stroke-width="1.1" fill="none"/></svg>
        melba@kalveria.com.sg
      </li>
      <li>
        <svg viewBox="0 0 14 14" aria-hidden="true"><circle cx="7" cy="7" r="6" fill="var(--brand-gold)"/><g stroke="#fff" stroke-width="0.9" fill="none"><ellipse cx="7" cy="7" rx="2.6" ry="6"/><path d="M1 7h12M2 4h10M2 10h10"/></g></svg>
        www.kalveria.com.sg
      </li>
    </ul>

    <address class="address">
      27 Kelso Street, #14-09<br>
      Harbourline Tower, Singapore<br>
      058217
    </address>

    <span class="ghost-name" aria-hidden="true">KALVERIA</span>
  </section>

  <section class="card card--back" aria-label="Business card back">
    <span class="brand-name">KALVERIA</span>
    <p class="website">www.kalveria.com.sg</p>
  </section>

</main>
</body>
</html>
```